Brimovex business card

Based on company logo and website given , to design a business card temple. Slogan "Your furry friends deserves the best"
Color style please refer to our website

```html
<!DOCTYPE html>
<html lang="en">
<head>
<meta charset="UTF-8">
<title>Brimovex business card</title>
<link rel="stylesheet" href="https://fonts.googleapis.com/css2?family=Cinzel:wght@400;600&display=swap">
<style>
  :root {
    --page: #e7e7e5;
    --card: #fbfbf8;
    --gold: #a3981c;
    --ink: #262626;
    --rule: #3a3a3a;
  }
  * { margin: 0; padding: 0; box-sizing: border-box; }
  html, body { width: 1200px; height: 900px; overflow: hidden; }
  body {
    background: var(--page);
    font-family: "Cinzel", "Times New Roman", serif;
    position: relative;
  }
  .card {
    position: absolute;
    width: 500px;
    height: 286px;
    background: var(--card);
    box-shadow: 0 2px 6px rgba(0,0,0,.08);
  }
  .card--front { left: 350px; top: 120px; }
  .card--back { left: 350px; top: 494px; }

  /* front */
  .front-brand {
    position: absolute;
    left: 0; right: 0; top: 82px;
    text-align: center;
  }
  .wordmark {
    color: var(--gold);
    font-weight: 600;
    line-height: 1;
  }
  .front-brand .wordmark { font-size: 60px; letter-spacing: 1px; }
  .slogan {
    margin-top: 6px;
    color: var(--ink);
    text-align: center;
  }
  .slogan__main { font-size: 18px; letter-spacing: 3px; line-height: 1.2; }
  .slogan__sub {
    display: flex; align-items: center; justify-content: center; gap: 12px;
    font-size: 11px; letter-spacing: 3px; margin-top: 2px;
  }
  .slogan__sub::before, .slogan__sub::after {
    content: ""; width: 36px; height: 1px; background: var(--gold);
  }

  /* back */
  .back-brand { position: absolute; left: 36px; top: 150px; }
  .back-brand .wordmark { font-size: 40px; }
  .divider {
    position: absolute; left: 262px; width: 1px; background: var(--rule);
  }
  .divider--top { top: 0; height: 44px; }
  .divider--bottom { bottom: 0; height: 60px; }
  .contact-list {
    position: absolute; left: 252px; top: 58px;
    list-style: none;
  }
  .contact-item {
    display: flex; align-items: center; gap: 14px;
    height: 32px;
  }
  .contact-item svg { width: 20px; height: 20px; fill: var(--ink); flex: none; }
  .contact-item span {
    color: var(--gold); font-size: 14px; letter-spacing: 1px;
  }
</style>
</head>
<body>
  <section class="card card--front">
    <div class="front-brand">
      <div class="wordmark">Brimovex</div>
      <div class="slogan">
        <div class="slogan__main">YOUR FURRY FRIENDS</div>
        <div class="slogan__sub">DESERVES THE BEST</div>
      </div>
    </div>
  </section>

  <section class="card card--back">
    <div class="back-brand"><div class="wordmark">Brimovex</div></div>
    <div class="divider divider--top"></div>
    <div class="divider divider--bottom"></div>
    <ul class="contact-list">
      <li class="contact-item">
        <svg viewBox="0 0 20 20" aria-label="Address"><path d="M10 2a5.5 5.5 0 0 0-5.5 5.5C4.5 12 10 18 10 18s5.5-6 5.5-10.5A5.5 5.5 0 0 0 10 2zm0 7.6a2 2 0 1 1 0-4 2 2 0 0 1 0 4z"/></svg>
        <span>XXX-X-XXXXXXXX-XXXX</span>
      </li>
      <li class="contact-item">
        <svg viewBox="0 0 20 20" aria-label="Phone"><path d="M6.2 3l2.2 3.2-1.3 1.5c.8 1.8 2.2 3.3 4 4.2l1.5-1.3L16 12.8l-1.4 2.6c-.3.5-.9.7-1.5.6C8.3 14.8 5 11.5 4 6.9c-.1-.6.1-1.2.6-1.5z"/></svg>
        <span>XXX-XXX-XX</span>
      </li>
      <li class="contact-item">
        <svg viewBox="0 0 20 20" aria-label="Mobile"><path d="M6.5 2h7a1 1 0 0 1 1 1v14a1 1 0 0 1-1 1h-7a1 1 0 0 1-1-1V3a1 1 0 0 1 1-1zm.5 2v11h6V4z"/></svg>
        <span>XXX-XXX-XXXX</span>
      </li>
      <li class="contact-item">
        <svg viewBox="0 0 20 20" aria-label="Email"><path d="M2.5 5h15v10h-15zm1.4 1.2L10 11l6.1-4.8z" fill-rule="evenodd"/></svg>
        <span>XXX-XXXXX-XXXX-XXXXXX</span>
      </li>
      <li class="contact-item">
        <svg viewBox="0 0 20 20" aria-label="Website"><path d="M10 2a8 8 0 1 0 0 16 8 8 0 0 0 0-16zm0 1.4c.9 1 1.6 2.9 1.8 5.1H8.2c.2-2.2.9-4.1 1.8-5.1zM3.5 9.3h3.3c.1-2.1.6-3.9 1.3-5A6.6 6.6 0 0 0 3.5 9.3zm0 1.4a6.6 6.6 0 0 0 4.6 5c-.7-1.1-1.2-2.9-1.3-5zm4.7 0h3.6c-.2 2.2-.9 4.1-1.8 5.1-.9-1-1.6-2.9-1.8-5.1zm5 0c-.1 2.1-.6 3.9-1.3 5a6.6 6.6 0 0 0 4.6-5zm3.3-1.4a6.6 6.6 0 0 0-4.6-5c.7 1.1 1.2 2.9 1.3 5z"/></svg>
        <span>XXXX-XXX-XZXX-XXXXXX</span>
      </li>
    </ul>
  </section>
</body>
</html>
```